Mock up Blog Design for midwife that works in a hospital setting

We are looking to have a design created for a midwife. This blog will be used to share information or experiences related to pregnancy, child birth and motherhood with its readership. It should convey a feeling of warmth and security to women who are looking for a partner in the birthing processes.

We are asking you to design the layout, not code it up. This is a concept project only.

NOtes from the midwife

​So I'm just going to put in links to a few blogs and say what I like and don't like about each one:

pelwinhartcote.com.au/blog/

I like how there is a colorful background that has to do with her books; maybe mine could have a background with baby stuff in the background. It's also nice how there's an index of recent postings with the subject listed and how the postings are sorted by date, all on the same page.

www.brightbottlejournal.com

I like that this one is set up like a website with tabs for resources, a bio, reader comments, etc.

freshparentnotes.tallowgrove.org

This blog has a very calming color scheme, which is welcoming. I like that there's a picture for every posting, and that at the bottom of the posting there is a little glossary with the subjects that are covered in the posting. Also, I like the way that the date of each blog is done.

laboursidechats.blogspot.com

This one is really funny, and similar in intention to the one that I want to do. I like that she has a glossary of medical terms so that readers can look them up.

General comments:
I'm not sure how much TBWH wants their logo on my blog or in the blog name...
I would like to be able to vet comments before they appear on the blog, so that if there's an inappropriate one, I can screen it out.
I would also like to be able to see how many people have viewed the site.
Updates

Target Market(s)

Pregnant mothers, new moms, hopeful moms

Industry/Entity Type

Hospital

Requirements
Must have
• Incorporation of the logo and at least one of the photographs that will be provided In the header
Should not have
• Should not look canned, rigid or boxy.

```html
<!DOCTYPE html>
<html lang="en">
<head>
<meta charset="utf-8">
<title>Brightwater Midwifery – Blog</title>
<link rel="stylesheet" href="https://fonts.googleapis.com/css2?family=Kalam:wght@400&family=Open+Sans:wght@300;400;600&display=swap">
<style>
  :root{
    --page-bg:#f3e0e2;
    --paper:#f7f8fa;
    --ink:#3d3d3d;
    --ink-soft:#5b5b5b;
    --teal-ink:#3f6070;
    --plum:#b14a7b;
    --plum-band:#b45783;
    --pink-tab:#eca9bd;
    --pink-soft:#eaa2b4;
    --mint:#cfe1e0;
    --mint-line:#b9cfcd;
    --post-alt:#ebe3e6;
    --link:#4c6f86;
    --photo-a:#f3e6e4;
    --photo-b:#c9a497;
  }
  *{box-sizing:border-box;margin:0;padding:0}
  html,body{width:1200px;height:993px;overflow:hidden}
  body{background:var(--page-bg);font-family:"Open Sans",sans-serif;color:var(--ink);position:relative}
  .sheet{position:absolute;left:320px;top:0;width:562px;height:984px;background:var(--paper);border-radius:0 0 14px 14px;box-shadow:0 2px 8px rgba(120,80,90,.18)}
  .masthead{position:absolute;left:0;top:0;width:562px;height:183px}
  .brand{position:absolute;left:0;top:0;width:228px;height:183px;background:#f6f7f9;display:flex;align-items:center;justify-content:center;gap:8px}
  .brand-dot{width:16px;height:16px;border-radius:50%;background:var(--plum)}
  .brand-name{font-weight:600;font-size:19px;line-height:1.15;color:var(--teal-ink)}
  .hero-photo{position:absolute;left:228px;top:0;width:334px;height:183px;background:linear-gradient(160deg,#fbfbfb 20%,var(--photo-a) 50%,var(--photo-b) 100%)}
  .navbar{position:absolute;left:0;top:183px;width:562px;height:31px;background:var(--plum-band)}
  .nav-tab{position:absolute;top:-5px;height:36px;padding:0 12px;font-size:22px;line-height:36px;color:#fff}
  .nav-tab.is-active{left:16px;width:103px;background:var(--plum);text-align:center}
  .nav-tab.glossary{left:122px;width:105px;background:var(--pink-tab);color:#fdf1f4;top:0;height:31px;line-height:31px;font-size:20px}
  .nav-tab.about{left:230px;width:100px;background:var(--pink-tab);color:#fdf1f4;top:0;height:31px;line-height:31px;font-size:20px}
  .search{position:absolute;left:404px;top:6px;width:144px;height:18px;background:#fff;border-radius:3px}
  .search svg{position:absolute;right:5px;top:3px}
  .main{position:absolute;left:0;top:214px;width:372px}
  .post{position:relative;padding:0 17px 0 16px}
  .post-date{position:absolute;left:-34px;width:44px;height:34px;text-align:center;font-size:13px;line-height:14px;padding-top:3px;box-shadow:2px 2px 2px rgba(0,0,0,.12)}
  .post-date b{display:block;font-size:12px}
  .post-date.teal{background:var(--mint);color:#555}
  .post-date.pink{background:var(--pink-soft);color:#fff}
  .post-title{font-family:"Kalam",cursive;font-weight:400;font-size:25px;color:var(--ink);letter-spacing:.5px}
  .post-photo{width:339px;height:173px;margin-top:4px;background:linear-gradient(90deg,#ffffff 0%,#f7dfe6 55%,#f1c8cf 100%);border:1px solid #ddd}
  .post p{font-size:12.6px;line-height:15.8px;text-align:justify;margin-top:12px;font-weight:400;color:var(--ink)}
  .post a{color:var(--link)}
  .share{display:flex;align-items:center;margin-top:16px;height:19px}
  .share-item{display:flex;align-items:flex-end;margin-right:6px;font-size:8px;color:#666}
  .share-item span{display:block;width:19px;height:19px;border-radius:2px;margin-right:1px}
  .s1{background:#3f5f98}.s2{background:#4aa0d4}.s3{background:#c4242d}.s4{background:#2f5779}
  .comment-btn{margin-left:auto;display:flex;align-items:center;font-size:8px;color:#666}
  .comment-btn span{margin-left:2px;background:var(--pink-soft);color:#fff;font-size:12.5px;padding:1px 9px;height:19px;width:80px;text-align:center}
  .post.first{padding-top:18px}
  .post.first .post-date{top:18px}
  .rule{height:3px;background:#dfe1e4;margin-top:9px}
  .post.second{background:var(--post-alt);padding-top:18px;padding-bottom:8px}
  .post.second .post-date{top:18px}
  .post.second p{margin-top:8px}
  .older{padding:16px 18px;font-size:17px;color:var(--teal-ink);border-top:3px solid #dfe1e4}
  .sidebar{position:absolute;left:390px;top:214px;width:172px;height:770px;background:var(--mint);border-radius:0 0 14px 14px}
  .feed{position:absolute;left:17px;top:10px;width:139px;height:152px;background:#fff;border:1px solid #dde;border-radius:3px;font-size:7px;color:#333}
  .feed-head{display:flex;justify-content:space-between;align-items:center;padding:5px 7px;font-size:12px;font-weight:600;border-bottom:1px solid #e5e5e5}
  .feed-follow{font-size:7px;font-weight:400;background:#e9eef3;padding:1px 4px;border-radius:2px}
  .feed-item{display:flex;gap:3px;padding:5px 7px 4px;border-bottom:1px solid #e5e5e5}
  .feed-avatar{width:22px;height:22px;border:1px solid #ccc;flex:none}
  .feed-meta{display:flex;justify-content:space-between;width:100%;font-weight:600}
  .feed-text{font-size:6.3px;line-height:8px;padding:0 7px 4px}
  .feed-input{position:absolute;left:4px;bottom:5px;width:130px;height:18px;border:1px solid #ddd;border-radius:3px;font-size:6.5px;color:#888;line-height:16px;padding-left:6px}
  .side-title{position:absolute;left:17px;font-size:16px;font-weight:600;color:#555}
  .comments{position:absolute;left:17px;top:218px;width:140px;font-size:10px;line-height:13px;color:var(--link)}
  .comments li{list-style:none;margin-bottom:3px}
  .comments b{font-weight:600;color:#666}
  .side-rule{position:absolute;left:0;top:312px;width:172px;height:2px;background:var(--mint-line)}
  .archives{position:absolute;left:16px;top:350px;font-size:13px;line-height:16.5px;color:#444;list-style:none}
  .archives .tri{display:inline-block;width:0;height:0;border-left:5px solid #666;border-top:4px solid transparent;border-bottom:4px solid transparent;margin-right:3px}
  .archives .sub{padding-left:10px}
  .archives .post-link{padding-left:29px;color:var(--link)}
</style>
</head>
<body>
<div class="sheet">
  <header class="masthead">
    <div class="brand"><span class="brand-dot"></span><span class="brand-name">Brightwater<br>Midwifery</span></div>
    <div class="hero-photo" role="img" aria-label="Family photo of parents with their five young children"></div>
    <nav class="navbar">
      <span class="nav-tab is-active">Home</span>
      <span class="nav-tab glossary">Glossary</span>
      <span class="nav-tab about">About</span>
      <div class="search"><svg width="12" height="12" viewBox="0 0 12 12"><circle cx="5" cy="5" r="3.5" fill="none" stroke="#555" stroke-width="1.5"/><line x1="7.5" y1="7.5" x2="11" y2="11" stroke="#555" stroke-width="2"/></svg></div>
    </nav>
  </header>

  <main class="main">
    <article class="post first">
      <div class="post-date teal">Mar<b>19</b></div>
      <h2 class="post-title">Hey who’s there?</h2>
      <div class="post-photo" role="img" aria-label="Toddler in pink lifting the shirt of a pregnant belly"></div>
      <p>The experience of giving birth can differ from one woman to another, and even for the same woman from one pregnancy to the next. Although there's no way to know how a woman's labor will progress or how long it will last, it's not unusual to be fearful of the process and worried about the pain associated with it.</p>
      <p>"We don't really know what mechanisms bring on labor," said Maren Holloway, a certified nurse midwife and the director of midwifery at Eastfield Health Network in Eastfield, Ore. "Science hasn't figured this out yet."</p>
      <p>Exactly what triggers labor is unclear.. <a href="#">Read more</a></p>
      <div class="share">
        <span class="share-item"><span class="s1"></span>3</span>
        <span class="share-item"><span class="s2"></span>8</span>
        <span class="share-item"><span class="s3"></span>1</span>
        <span class="share-item"><span class="s4"></span></span>
        <span class="comment-btn">6<span>Comment</span></span>
      </div>
      <div class="rule"></div>
    </article>

    <article class="post second">
      <div class="post-date pink">Mar<b>17</b></div>
      <h2 class="post-title">Getting help after the birth</h2>
      <p>Consider getting help during this time, which can be very hectic and overwhelming. While in the hospital, talk to the experts around you. Many hospitals have feeding specialists or lactation consultants who can help you get started nursing or bottle-feeding. In addition, nurses are a great resource to show you how to hold, burp, change, and care for your baby.. <a href="#">Read more</a></p>
      <div class="share">
        <span class="share-item"><span class="s1"></span>7</span>
        <span class="share-item"><span class="s2"></span>2</span>
        <span class="share-item"><span class="s3"></span>9</span>
        <span class="share-item"><span class="s4"></span></span>
        <span class="comment-btn">11<span>Comment</span></span>
      </div>
    </article>
    <div class="older">‹ Older Posts</div>
  </main>

  <aside class="sidebar">
    <div class="feed">
      <div class="feed-head">Updates <span class="feed-follow">Follow</span></div>
      <div class="feed-item"><div class="feed-avatar"></div><div class="feed-meta"><span>Brightwater<br>@Brightwater</span><span>22 Feb</span></div></div>
      <div class="feed-text">Hey I've just posted a new article on my blog about how to stay fit while being a mother of a lovely bunch of children! Check it out :)</div>
      <div class="feed-item"><div class="feed-avatar"></div><div class="feed-meta"><span>Brightwater<br>@Brightwater</span><span>22 Feb</span></div></div>
      <div class="feed-input">Reply to @Brightwater</div>
    </div>
    <h3 class="side-title" style="top:205px;transform:translateY(-16px)">Recent comments</h3>
    <ul class="comments">
      <li><b>today</b> by <b>Emily</b>: How do you manage to raise...</li>
      <li><b>today</b> by <b>Sarah</b>: My belly is so huge now, help!</li>
      <li><b>yesterday</b> by <b>Jen</b>: I plan to give birth to a dozen of...</li>
    </ul>
    <div class="side-rule"></div>
    <h3 class="side-title" style="top:330px">Archives</h3>
    <ul class="archives">
      <li><span class="tri"></span>2015 (2)</li>
      <li class="sub"><span class="tri"></span>March</li>
      <li class="sub"><span class="tri"></span>February</li>
      <li class="post-link">Best baby post</li>
      <li><span class="tri"></span>2014 (82)</li>
      <li><span class="tri"></span>2013 (11)</li>
    </ul>
  </aside>
</div>
</body>
</html>
```